Join Wait / Reservations Handout

This is a handout for guests with information about the ability to join our
waitlist and/or make reservations. It will be handed out to any guest that ends up waiting on our waitlist to be seated. It will describe how our waitlist and reservations system works. It is informational for them to download our mobile app.

It was forcing me to move the look and feel sliders. Please refer to our branding guide for look and feel.

Industry/Entity Type

Hospitality

Contact Information for Business Card

One of the attached documents give a very generic layout of the information we need on this card. This layout is more for where we wanted the information placed and has nothing to do with the design aspects of the piece. Please use your imagination. Any of the 5 colors in the branding guide can be used anywhere. The pineapple design can be used anywhere in any color combination.

If you require any other files please let me know. Thanks

Font styles to use
Other font styles liked:
• Please see attached branding guide

Requirements
Must have
• The only color requirement is that the logo be the blue with teal lettering...This has to match our app store logo.

```html
<!DOCTYPE html>
<html lang="en">
<head>
<meta charset="utf-8">
<title>Harborline Eatery – Business Card</title>
<link rel="stylesheet" href="https://fonts.googleapis.com/css2?family=Lato:wght@400;700&display=swap">
<style>
  :root {
    --navy: #0c3550;
    --navy-deep: #04344c;
    --teal: #5fa8ad;
    --ink: #1f2a33;
    --paper: #ffffff;
    --backdrop: #e9ebed;
  }
  * { margin: 0; padding: 0; box-sizing: border-box; }
  html, body { width: 1200px; height: 900px; overflow: hidden; }
  body {
    background: var(--backdrop);
    font-family: "Lato", Arial, sans-serif;
    position: relative;
  }
  .card { position: absolute; overflow: hidden; }
  .card-front {
    left: 78px; top: 35px; width: 587px; height: 362px;
    background: var(--paper);
  }
  .card-back {
    left: 388px; top: 505px; width: 567px; height: 352px;
    background: var(--navy-deep);
  }

  .brand {
    position: absolute;
    width: 300px;
    display: flex; flex-direction: column; align-items: center;
    font-weight: 700; text-transform: uppercase; text-align: center;
  }
  .brand-dot { width: 26px; height: 26px; border-radius: 50%; background: var(--teal); margin-bottom: 44px; }
  .brand-name { font-size: 31px; letter-spacing: 3px; line-height: 38px; }
  .card-front .brand { left: 280px; top: 48px; color: var(--navy); }
  .card-back .brand { left: 134px; top: 108px; color: var(--paper); }

  .holder { position: absolute; left: 27px; top: 185px; }
  .holder-name { font-size: 21px; font-weight: 700; letter-spacing: 0.3px; color: var(--navy); }
  .holder-title { font-size: 16.5px; color: var(--ink); margin-top: 0; }

  .accent-left { position: absolute; left: 0; top: 247px; width: 10px; height: 74px; background: var(--navy); }
  .accent-right { position: absolute; right: 0; top: 288px; width: 11px; height: 34px; background: var(--teal); }

  .contact-list { position: absolute; left: 27px; top: 241px; list-style: none; font-size: 16.5px; color: var(--ink); }
  .contact-list li { display: flex; align-items: center; gap: 6px; height: 21.5px; }
  .contact-list svg { width: 12px; height: 12px; fill: var(--navy); flex: none; }

  .address {
    position: absolute; right: 24px; top: 283px;
    text-align: right; font-size: 16.5px; line-height: 21.5px; color: var(--ink);
  }
</style>
</head>
<body>

<section class="card card-front">
  <div class="brand"><span class="brand-dot"></span><span class="brand-name">Harborline<br>Eatery</span></div>

  <div class="holder">
    <p class="holder-name">DANIEL REYES</p>
    <p class="holder-title">Managing Director</p>
  </div>

  <span class="accent-left"></span>

  <ul class="contact-list">
    <li><svg viewBox="0 0 12 12" aria-hidden="true"><path d="M1 3c0-1 1-2 2-2h6c1 0 2 1 2 2v1H8V3H4v1H1zM2 5h8l1 6H1z"/></svg>(044)123456789</li>
    <li><svg viewBox="0 0 12 12" aria-hidden="true"><path d="M3 0h6v4H3zM1 4h10v6H9v2H3v-2H1zM4 8v3h4V8z"/></svg>(044)123456789</li>
    <li><svg viewBox="0 0 12 12" aria-hidden="true"><path d="M0 2h12v1L6 7 0 3zM0 4l6 4 6-4v6H0z"/></svg>info@youremail.com</li>
    <li><svg viewBox="0 0 12 12" aria-hidden="true"><circle cx="6" cy="6" r="5.5"/><path d="M1 6h10M6 1v10" stroke="#fff" stroke-width="0.9" fill="none"/><ellipse cx="6" cy="6" rx="2.3" ry="5" stroke="#fff" stroke-width="0.9" fill="none"/></svg>www.websitename.com</li>
  </ul>

  <div class="address">
    <p>1234, Address GoesHere</p>
    <p>Country name, 12345</p>
  </div>

  <span class="accent-right"></span>
</section>

<section class="card card-back">
  <div class="brand"><span class="brand-dot"></span><span class="brand-name">Harborline<br>Eatery</span></div>
</section>

</body>
</html>
```